Online Fashion Boutique needs new Logo and Business Card Design

Morvel Boutique is a brand new boutique based in the UK.

We offer unique fashionable clothing, shoes and accessories for ladies.

For the design, I'll like a drawing/illustration of a fashionable lady with shopping bag(s) wearing heels and to the side "Morvel Boutique" under that "wear it your own way". My preferred colours are Pink and Black and White(more like the Zebra print). I want the design to portray Stylish, Chic and Unique.

Industry/Entity Type

Boutique

```html
<!DOCTYPE html>
<html lang="en">
<head>
<meta charset="utf-8">
<title>Morvel Boutique – Business Card</title>
<link rel="stylesheet" href="https://fonts.googleapis.com/css2?family=Josefin+Sans:wght@400;600&display=swap">
<style>
  :root {
    --page-bg: #f1f1f1;
    --cream: #fbf6d9;
    --cream-light: #ffffff;
    --band-yellow: #fde48a;
    --brand-pink: #ef1b8c;
    --ink: #2a2a2a;
    --card-shadow: rgba(0, 0, 0, 0.25);
  }
  * { box-sizing: border-box; margin: 0; padding: 0; }
  html, body {
    width: 1200px;
    height: 1000px;
    overflow: hidden;
    background: var(--page-bg);
    font-family: "Josefin Sans", "Century Gothic", sans-serif;
  }
  .stage {
    width: 1200px;
    height: 1000px;
    display: flex;
    align-items: center;
    justify-content: center;
    gap: 80px;
  }
  .card {
    position: relative;
    width: 420px;
    height: 720px;
    overflow: hidden;
    background: radial-gradient(ellipse at 50% 55%, var(--cream-light) 0%, var(--cream) 70%);
    box-shadow: 0 6px 18px var(--card-shadow);
  }
  .card-base {
    position: absolute;
    inset: 0;
    width: 100%;
    height: 100%;
  }
  .band-yellow { fill: var(--band-yellow); }
  .band-pattern { fill: var(--brand-pink); }

  /* Front */
  .brand {
    position: absolute;
    left: 0;
    right: 0;
    top: 150px;
    display: flex;
    flex-direction: column;
    align-items: center;
    gap: 18px;
  }
  .brand-row {
    display: flex;
    align-items: center;
    gap: 14px;
  }
  .brand-dot {
    width: 22px;
    height: 22px;
    border-radius: 50%;
    background: var(--brand-pink);
  }
  .brand-name {
    font-weight: 400;
    font-size: 40px;
    color: var(--brand-pink);
    letter-spacing: 1px;
  }
  .brand-tagline {
    font-weight: 400;
    font-size: 22px;
    letter-spacing: 6px;
    color: var(--ink);
  }

  /* Back */
  .contact-list {
    position: absolute;
    top: 70px;
    left: 70px;
    list-style: none;
    display: flex;
    flex-direction: column;
    gap: 22px;
  }
  .contact-item {
    display: flex;
    align-items: center;
    gap: 26px;
    font-size: 26px;
    letter-spacing: 1px;
    color: var(--ink);
  }
  .contact-icon {
    width: 34px;
    height: 34px;
    flex: none;
  }
  .contact-icon .stroke { fill: none; stroke: var(--brand-pink); stroke-width: 2.4; }
  .contact-icon .fill { fill: var(--brand-pink); }
</style>
</head>
<body>
<main class="stage">

  <section class="card card-front">
    <svg class="card-base" viewBox="0 0 420 720" preserveAspectRatio="none">
      <path class="band-yellow" d="M0 455 Q210 560 420 455 L420 720 L0 720 Z"/>
      <path class="band-pattern" role="img" aria-label="Pink swirl pattern band"
            d="M0 485 Q210 585 420 485 L420 720 L0 720 Z"/>
    </svg>
    <div class="brand">
      <div class="brand-row">
        <span class="brand-dot"></span>
        <h1 class="brand-name">Morvel Boutique</h1>
      </div>
      <p class="brand-tagline">wear it your own way</p>
    </div>
  </section>

  <section class="card card-back">
    <svg class="card-base" viewBox="0 0 420 720" preserveAspectRatio="none">
      <path class="band-yellow" d="M0 455 Q210 560 420 455 L420 720 L0 720 Z"/>
      <path class="band-pattern" role="img" aria-label="Pink swirl pattern band"
            d="M0 485 Q210 585 420 485 L420 720 L0 720 Z"/>
    </svg>
    <ul class="contact-list">
      <li class="contact-item">
        <svg class="contact-icon" viewBox="0 0 34 34" aria-label="Website">
          <circle class="fill" cx="17" cy="17" r="14"/>
          <path d="M10 12 Q15 9 18 13 Q16 17 12 16 Z M19 20 Q24 18 25 23 Q21 27 19 24 Z" fill="#fff"/>
        </svg>
        <span>text here</span>
      </li>
      <li class="contact-item">
        <svg class="contact-icon" viewBox="0 0 34 34" aria-label="Email">
          <rect class="stroke" x="4" y="8" width="26" height="18"/>
          <path class="stroke" d="M4 8 L17 19 L30 8 M4 26 L13 16 M30 26 L21 16"/>
        </svg>
        <span>text here</span>
      </li>
      <li class="contact-item">
        <svg class="contact-icon" viewBox="0 0 34 34" aria-label="Phone">
          <path class="fill" d="M9 5 L14 5 L15 11 L12 13 Q14 20 21 22 L23 19 L29 20 L29 25 Q28 29 24 29 Q8 27 5 10 Q5 6 9 5 Z"/>
        </svg>
        <span>text here</span>
      </li>
      <li class="contact-item">
        <svg class="contact-icon" viewBox="0 0 34 34" aria-label="Address">
          <path class="fill" d="M17 31 L8 17 A10 10 0 1 1 26 17 Z"/>
          <circle cx="17" cy="13" r="4" fill="#fff"/>
        </svg>
        <span>text here</span>
      </li>
      <li class="contact-item">
        <svg class="contact-icon" viewBox="0 0 34 34" aria-label="Fax">
          <rect class="stroke" x="4" y="12" width="26" height="17"/>
          <rect class="stroke" x="10" y="4" width="14" height="8"/>
          <path class="stroke" d="M9 18 H25 M9 23 H25"/>
        </svg>
        <span>text here</span>
      </li>
    </ul>
  </section>

</main>
</body>
</html>
```